Football / Soccer Service related website

I would like my website updated.
The current URL is https://brivanta.global

It will also need to include a blog in the menu.

I have attached my brand guidelines.

As this is aimed at professional football players I am looking for something that looks particularly affluent and ahead of it's time.

I want it to look great desktop and mobile. However, it is particularly important to look great on mobile as most players will be accessing it from their mobile devices.

It must be within my attached brand guidelines and I want an affluent look. Think premium watch websites such as quellor.com etc.

Target Market(s)

High level professional Footballers

Coding

Number of Pages Required

Colors
ffffff

Requirements
Must have
• The website is already exists and needs to be updated within my brand guidelines (see attached).

The majority of visitors to the website will be on mobile. Whilst I still want it to look great on desktop I want it to have a wow factor on mobile most importantly.

With color scale, please see brand guidelines
Nice to have
• As I am aiming at an affluent market who are already interested in high end designer labels I would like a similar feel.

I'm thinking a look like a designer watch website such as quellor.com (please note this is a suggestion that it should have a feel of designer and high end... not to replicate quellor.com).
Should not have
• Anything tack or cartoon like

```html
<!DOCTYPE html>
<html lang="en">
<head>
<meta charset="utf-8">
<title>Brivanta — Brain Performance for Footballers</title>
<link rel="stylesheet" href="https://fonts.googleapis.com/css2?family=Roboto:wght@300;400;500;700;900&display=swap">
<style>
:root{
  --blue:#1a86d6;
  --blue-dark:#0f5fa8;
  --ink:#1b1b1b;
  --text:#555;
  --muted:#888;
  --night:#161616;
  --white:#fff;
}
*{box-sizing:border-box;margin:0;padding:0}
html,body{width:1200px;height:3824px;overflow:hidden}
body{font-family:"Roboto",Arial,sans-serif;color:var(--text);background:var(--white);position:relative}
.abs{position:absolute}
a{color:inherit;text-decoration:none}

/* hero */
.hero{position:absolute;left:0;top:0;width:1200px;height:680px;background:radial-gradient(ellipse at 70% 35%,#8a8a8a 0%,#4b4b4b 35%,#1e1e1e 75%,#111 100%)}
.nav{position:absolute;top:0;left:0;width:1200px;height:64px;font-size:14px;font-weight:500;color:var(--white)}
.nav .brand-small{position:absolute;left:112px;top:24px;color:var(--blue)}
.nav .item{position:absolute;top:24px;white-space:nowrap}
.logo{display:flex;align-items:center;gap:10px;color:var(--white);font-weight:900;font-size:26px;letter-spacing:1px;white-space:nowrap}
.logo .dot{width:32px;height:32px;border-radius:50%;background:var(--white)}
.hero h1{position:absolute;left:112px;top:290px;color:var(--white);font-size:40px;font-weight:900;letter-spacing:1px}
.hero p{position:absolute;left:112px;top:346px;width:470px;color:#ddd;font-size:17px;line-height:27px}
.hero .more{position:absolute;left:112px;top:420px;color:var(--blue);font-size:16px}

/* mindset */
.mindset h2{position:absolute;left:0;width:1200px;top:770px;text-align:center;font-size:34px;font-weight:700;color:var(--ink)}
.mindset p{position:absolute;left:160px;width:880px;font-size:14px;line-height:24px}
.mindset .strong{font-size:20px;font-weight:700;color:var(--ink)}
.btn{position:absolute;display:flex;align-items:center;justify-content:center;gap:8px;border:2px solid var(--blue);border-radius:30px;color:var(--blue);font-weight:700;font-size:13px;letter-spacing:.5px}

/* programs */
.programs h3{position:absolute;left:112px;top:1116px;font-size:26px;font-weight:700;color:var(--ink)}
.programs .link{position:absolute;left:258px;top:1126px;color:var(--blue);font-size:13px;font-weight:700;letter-spacing:.5px;border-bottom:2px solid var(--blue)}
.card{position:absolute;top:1184px;width:308px;height:360px}
.card .photo{width:100%;height:260px}
.card .body{position:absolute;left:14px;top:250px;width:280px;background:var(--white);padding:14px 16px}
.card h4{font-size:16px;font-weight:700;color:var(--ink)}
.card p{font-size:12px;line-height:17px;color:var(--muted);margin-top:8px;width:200px}
.card .read{display:block;margin-top:12px;color:var(--blue);font-size:12px;font-weight:700}

/* about */
.about{position:absolute;left:0;top:1680px;width:1200px;height:460px;background:var(--night);overflow:hidden}
.about h2{position:absolute;left:112px;top:90px;font-size:42px;font-weight:700;color:var(--white)}
.about p{position:absolute;left:112px;top:160px;width:460px;font-size:14px;line-height:24px;color:#cfcfcf}

/* pillars */
.pillar{position:absolute}
.pillar .photo{width:100%;height:100%}
.caption{position:absolute;background:var(--white);box-shadow:0 6px 20px rgba(0,0,0,.12);text-align:center;padding:18px 24px}
.caption h5{font-size:15px;font-weight:700;color:var(--ink);letter-spacing:.5px}
.caption p{font-size:13px;line-height:20px;color:var(--muted);margin-top:8px}

/* author */
.author{position:absolute;left:0;top:3188px;width:1200px;height:260px;background:var(--blue)}
.author h2{position:absolute;left:112px;top:60px;font-size:30px;font-weight:700;color:var(--white)}
.author p{position:absolute;left:112px;top:112px;width:540px;font-size:14px;line-height:23px;color:#e6f2fc}

/* footer */
.footer{position:absolute;left:0;top:3448px;width:1200px;height:376px;background:var(--night)}
.footer .row{position:absolute;left:0;width:1200px;display:flex;justify-content:center;align-items:center;color:#ccc}
.contact{gap:110px;font-size:14px}
.contact span{display:flex;align-items:center;gap:10px}
.links{gap:14px;font-size:13px}
.copy{font-size:12px;color:#999;gap:10px}
.social{gap:14px}
.social i{width:36px;height:36px;border-radius:50%;border:2px solid #888;display:block}
</style>
</head>
<body>

<header class="hero">
  <div role="img" aria-label="Black and white photo of a footballer striking the ball in a floodlit stadium" class="abs" style="inset:0;background:linear-gradient(90deg,rgba(10,10,10,.75) 0%,rgba(10,10,10,.2) 55%,rgba(10,10,10,.35) 100%)"></div>
  <nav class="nav">
    <a class="brand-small" href="#">Brivanta Global</a>
    <a class="item" style="left:300px" href="#">Who is Neil Hartwick?</a>
    <a class="logo abs" style="left:498px;top:14px" href="#"><span class="dot"></span>BRIVANTA</a>
    <a class="item" style="left:752px" href="#">Reviews of Neil's Work</a>
    <a class="item" style="left:932px" href="#">Blog</a>
    <a class="item" style="left:984px" href="#">Contact</a>
    <svg class="abs" style="left:1052px;top:25px" width="15" height="15" viewBox="0 0 16 16" fill="none" stroke="#fff" stroke-width="2"><circle cx="6.5" cy="6.5" r="5"/><path d="M10.5 10.5 15 15"/></svg>
  </nav>
  <h1>BRIVANTA</h1>
  <p>what if it was simpler than you could imagine, but more effective than anything in the game.</p>
  <a class="more" href="#">Discover how it works</a>
</header>

<section class="mindset">
  <h2>Why This is Far More Than Mindset</h2>
  <p style="top:836px">When you think about your football mindset or Psychology you probably think of something that can have a few simple and slight changes to your game. Mindset has become such a buzz word, but it isn't simply mindset that helps players with</p>
  <p class="strong" style="top:906px">... It's brain performance.</p>
  <p style="top:950px">Let me ask you to think for one moment about what your brain is responsible for in Your life. On and off the pitch.</p>
  <a class="btn" href="#" style="left:152px;top:1000px;width:176px;height:48px">LEARN MORE
    <svg width="16" height="16" viewBox="0 0 16 16"><circle cx="8" cy="8" r="8" fill="#1a86d6"/><path d="M6.5 4.5 10 8l-3.5 3.5" stroke="#fff" stroke-width="2" fill="none"/></svg></a>
</section>

<section class="programs">
  <h3>Scoutline</h3>
  <a class="link" href="#">CHECK OUT THE 1-TO-1 PROGRAMS</a>
  <article class="card" style="left:112px">
    <div class="photo" role="img" aria-label="Portrait of a professional player in club kit" style="background:linear-gradient(160deg,#c9a56a,#6b4a2c 60%,#3a2a1e)"></div>
    <div class="body"><h4>Lorem ipsum dolor consectetur</h4><p>Sed ut perspiciatis unde omnis iste natus error sit</p><a class="read" href="#">READ MORE ›</a></div>
  </article>
  <article class="card" style="left:446px">
    <div class="photo" role="img" aria-label="Player training on a pitch with a ball" style="background:linear-gradient(180deg,#e9ecef,#b7bec4 55%,#4f6b3a)"></div>
    <div class="body"><h4>Lorem ipsum dolor consectetur</h4><p>Sed ut perspiciatis unde omnis iste natus error sit</p><a class="read" href="#">READ MORE ›</a></div>
  </article>
  <article class="card" style="left:780px">
    <div class="photo" role="img" aria-label="Player celebrating with arms raised in a stadium" style="background:linear-gradient(180deg,#8aa0b0,#c4a34c 55%,#3d5a2a)"></div>
    <div class="body"><h4>Lorem ipsum dolor consectetur</h4><p>Sed ut perspiciatis unde omnis iste natus error sit</p><a class="read" href="#">READ MORE ›</a></div>
  </article>
</section>

<section class="about">
  <svg class="abs" style="left:600px;top:0" width="600" height="460" viewBox="0 0 600 460"><polygon points="140,0 600,0 600,460 0,460" fill="#1a86d6"/></svg>
  <div role="img" aria-label="Photo of a player in a blue jersey" class="abs" style="left:740px;top:0;width:460px;height:460px;background:linear-gradient(90deg,rgba(15,95,168,0) 0%,rgba(15,60,110,.55) 45%,rgba(26,134,214,.2) 100%)"></div>
  <h2>About Us</h2>
  <p>Lorem ipsum dolor sit amet, consectetur adipiscing elit, sed do eiusmod tempor incididunt ut labore et dolore magna aliqua. Ut enim ad minim veniam, quis nostrud exercitation ullamco nisi ut aliquip ex ea commodo consequat. Duis aute irure dolor in reprehenderit in voluptate velit esse cillum dolore eu fugiat nulla pariatur. Excepteur sint occaecat cupidatat non proident, sunt in culpa qui officia deserunt mollit anim id est laborum.</p>
</section>

<section class="pillars">
  <div class="pillar" style="left:112px;top:2260px;width:476px;height:300px">
    <div class="photo" role="img" aria-label="Youth players competing for the ball" style="background:linear-gradient(170deg,#9fb2c2,#b54a4a 45%,#4e7a36)"></div>
  </div>
  <div class="caption" style="left:132px;top:2486px;width:436px">
    <h5>UNDERSTAND</h5><p>Simple to understand overview of your brain from a practical point of view</p>
  </div>
  <div class="pillar" style="left:612px;top:2260px;width:476px;height:300px">
    <div class="photo" role="img" aria-label="Close-up of a player's boot on the ball" style="background:linear-gradient(170deg,#3a4a3a,#6f7d4d 50%,#2e3d22)"></div>
  </div>
  <div class="caption" style="left:632px;top:2486px;width:436px">
    <h5>UNDERSTAND</h5><p>Simple to understand overview of your brain from a practical point of view</p>
  </div>
  <div class="pillar" style="left:112px;top:2692px;width:976px;height:348px">
    <div class="photo" role="img" aria-label="Players locked in a scrum under stadium lights" style="background:linear-gradient(180deg,#2a2a2a,#5a4f48 50%,#3c5a2c)"></div>
  </div>
  <div class="caption" style="left:112px;top:2930px;width:320px;text-align:left">
    <h5>CONDITION</h5><p>As we continue to implement effective ways of improving your brain, your brain will become</p>
  </div>
</section>

<section class="author">
  <h2>BEST SELLING AUTHOR</h2>
  <p>Neil's best selling book has been read by hundreds of pro players and thousands of amateur players. It is often referred to as the footballers bible and is even used by the University of Ashbury.</p>
  <div role="img" aria-label="Cover of the book by Neil Hartwick" class="abs" style="left:860px;top:-40px;width:200px;height:300px;background:linear-gradient(160deg,#2b3a55,#0e1526);box-shadow:0 12px 30px rgba(0,0,0,.35)"></div>
  <div class="abs" style="left:984px;top:-10px;width:56px;height:64px;background:#b0262c"></div>
</section>

<footer class="footer">
  <div class="row" style="top:60px"><a class="logo" href="#"><span class="dot"></span>BRIVANTA</a></div>
  <div class="row contact" style="top:128px">
    <span><svg width="14" height="18" viewBox="0 0 14 18"><path d="M7 0C3 0 0 3 0 7c0 5 7 11 7 11s7-6 7-11c0-4-3-7-7-7z" fill="#ccc"/><circle cx="7" cy="7" r="2.5" fill="#161616"/></svg>27 Harrow Lane, Ashbury AB1 2CD</span>
    <span><svg width="16" height="16" viewBox="0 0 16 16"><path d="M3 1l3 3-2 2c1 2 3 4 5 5l2-2 3 3-2 3C6 15 1 10 0 3z" fill="#ccc"/></svg>+44 (0) 555 010 0199</span>
    <span><svg width="18" height="14" viewBox="0 0 18 14"><rect width="18" height="14" rx="2" fill="#ccc"/><path d="M1 2l8 6 8-6" stroke="#161616" stroke-width="1.5" fill="none"/></svg>neil@neilhartwick.org</span>
  </div>
  <div class="row links" style="top:180px">
    <a href="#">Home</a><span>|</span><a href="#">Work Personally With Neil</a><span>|</span><a href="#">Who is Neil Hartwick?</a><span>|</span><a href="#">Reviews of Neil's Work</a><span>|</span><a href="#">Contact Us</a>
  </div>
  <div class="row copy" style="top:222px">© 2019 Brivanta Global. All Rights Reserved <span>|</span> Privacy Policy <span>|</span> Terms &amp; Condition</div>
  <div class="row social" style="top:264px"><i></i><i></i><i></i><i></i></div>
</footer>

</body>
</html>
```